Horse related business entrepreneur needs a business card

I need a business card design for my horse related business. The enterprise is Copper Vale LLC and I have 3 businesses (headquartered at 2 locations): 1. property management where we rent horse stalls and apartments at a thoroughbred training center outside Ocala; 2. a medium sized transportation service in central Florida that sells horse bedding and removes used horse bedding from horse farms; and horse racing

```html
<!DOCTYPE html>
<html lang="en">
<head>
<meta charset="utf-8">
<title>Copper Vale LLC – Business Cards</title>
<link href="https://fonts.googleapis.com/css2?family=Open+Sans:wght@400;700&family=Questrial&family=Montserrat:wght@700&display=swap" rel="stylesheet">
<style>
  :root {
    --ink: #221f20;
    --paper: #ffffff;
    --gold: #d4b06a;
    --copper: #ec9654;
    --band-text: #2b2826;
    --horse-brown: #5a2d18;
    --horse-deep: #3a1c10;
  }
  html, body {
    margin: 0; padding: 0;
    width: 1200px; height: 1200px;
    overflow: hidden;
    background: var(--paper);
  }
  .sheet { position: relative; width: 1200px; height: 1200px; }

  .card {
    position: absolute;
    width: 582px; height: 358px;
    background: var(--ink);
    overflow: hidden;
  }
  .card--gold { --accent: var(--gold); }
  .card--copper { --accent: var(--copper); }
  .pos-a { left: 2px; top: 226px; }
  .pos-b { left: 618px; top: 226px; }
  .pos-c { left: 2px; top: 620px; }
  .pos-d { left: 618px; top: 620px; }

  /* front */
  .herd-faint {
    position: absolute; left: 200px; top: 170px; width: 382px; height: 188px;
    background: radial-gradient(ellipse at 55% 60%, rgba(90,45,24,0.55), rgba(58,28,16,0.25) 55%, rgba(34,31,32,0) 80%);
  }
  .rearing-horse {
    position: absolute; left: 308px; top: 58px; width: 250px; height: 244px;
    background: radial-gradient(ellipse at 50% 50%, var(--accent) 0%, var(--accent) 45%, rgba(0,0,0,0) 72%);
  }
  .title-tab {
    position: absolute; left: 420px; top: 0; width: 6px; height: 64px;
    background: var(--paper);
  }
  .person {
    position: absolute; left: 426px; top: 20px; width: 156px;
    text-align: center; color: var(--paper);
  }
  .person__name { font-family: "Questrial", sans-serif; font-size: 26px; line-height: 30px; }
  .person__role { font-family: "Montserrat", sans-serif; font-weight: 700; font-size: 15px; line-height: 16px; }

  .id-panel {
    position: absolute; left: 0; top: 62px; width: 222px; height: 234px;
    border-radius: 0 56px 12px 0; overflow: hidden;
    background: var(--paper);
  }
  .id-panel__mark {
    position: absolute; left: 90px; top: 30px; width: 37px; height: 37px;
    border: 2px solid var(--ink); border-radius: 50%;
  }
  .id-panel__name {
    position: absolute; left: 0; width: 222px; top: 84px; text-align: center;
    font-family: "Open Sans", sans-serif; font-weight: 700; font-size: 25px; color: var(--ink);
  }
  .id-panel__tagline {
    position: absolute; left: 0; width: 222px; top: 124px; text-align: center;
    font-family: "Open Sans", sans-serif; font-size: 11px; color: var(--ink);
  }
  .card--copper .id-panel__tagline { color: var(--copper); }
  .contact {
    position: absolute; left: 0; top: 166px; width: 222px; height: 68px;
    background: var(--accent); box-sizing: border-box; padding: 8px 0 0 34px;
    font-family: "Open Sans", sans-serif; font-size: 12.5px; line-height: 17.5px; color: var(--band-text);
  }

  /* back */
  .herd {
    position: absolute; left: 0; top: 38px; width: 582px; height: 236px;
    background: linear-gradient(90deg, rgba(110,55,25,0.9), rgba(80,38,20,0.95) 35%, rgba(125,62,30,0.9) 65%, rgba(70,34,18,0.9));
    border-radius: 40% 45% 0 0 / 30% 35% 0 0;
  }
  .mini-brand {
    position: absolute; left: 52px; top: 28px; width: 88px; text-align: center; color: var(--paper);
  }
  .mini-brand__mark { width: 13px; height: 13px; background: var(--paper); border-radius: 50%; margin: 0 auto 4px; }
  .mini-brand__name { font-family: "Open Sans", sans-serif; font-weight: 700; font-size: 9.5px; line-height: 11px; }
  .mini-brand__tagline { font-family: "Open Sans", sans-serif; font-size: 4px; line-height: 5px; }
  .address-band {
    position: absolute; left: 0; top: 274px; width: 582px; height: 84px;
    background: var(--accent);
    font-family: "Questrial", sans-serif; font-size: 19.5px; line-height: 24px; color: var(--band-text);
  }
  .address { position: absolute; top: 16px; }
  .address--va { left: 66px; }
  .address--fl { left: 326px; }
  .address sup { font-size: 9px; vertical-align: 9px; line-height: 0; }
  .address-band__rule {
    position: absolute; left: 304px; top: 16px; width: 2px; height: 50px; background: var(--band-text);
  }
</style>
</head>
<body>
<main class="sheet">

  <section class="card card--gold pos-a">
    <div class="herd-faint" role="img" aria-label="Faded photo of running horses"></div>
    <div class="rearing-horse" role="img" aria-label="Gold silhouette of a rearing horse"></div>
    <div class="title-tab"></div>
    <div class="person"><div class="person__name">Dana Whitlow</div><div class="person__role">Owner</div></div>
    <div class="id-panel">
      <div class="id-panel__mark"></div>
      <div class="id-panel__name">Copper Vale LLC</div>
      <div class="id-panel__tagline">(AN EQUINE CONGLOMERATE)</div>
      <div class="contact">dana@coppervale.com<br>p: (555) 014-7051<br>f: (555) 014-0402</div>
    </div>
  </section>

  <section class="card card--copper pos-b">
    <div class="herd-faint" role="img" aria-label="Faded photo of running horses"></div>
    <div class="rearing-horse" role="img" aria-label="Orange silhouette of a rearing horse"></div>
    <div class="title-tab"></div>
    <div class="person"><div class="person__name">Dana Whitlow</div><div class="person__role">Owner</div></div>
    <div class="id-panel">
      <div class="id-panel__mark"></div>
      <div class="id-panel__name">Copper Vale LLC</div>
      <div class="id-panel__tagline">(AN EQUINE CONGLOMERATE)</div>
      <div class="contact">dana@coppervale.com<br>p: (555) 014-7051<br>f: (555) 014-0402</div>
    </div>
  </section>

  <section class="card card--gold pos-c">
    <div class="herd" role="img" aria-label="Photo of chestnut horses galloping"></div>
    <div class="mini-brand"><div class="mini-brand__mark"></div><div class="mini-brand__name">Copper Vale LLC</div><div class="mini-brand__tagline">(AN EQUINE CONGLOMERATE)</div></div>
    <div class="address-band">
      <div class="address address--va">4120 Maple Hollow Way<br>Riverton, VA 22950</div>
      <div class="address-band__rule"></div>
      <div class="address address--fl">2750 SE 112<sup>th</sup> Terrace<br>Pinecrest, FL 32690</div>
    </div>
  </section>

  <section class="card card--copper pos-d">
    <div class="herd" role="img" aria-label="Photo of chestnut horses galloping"></div>
    <div class="mini-brand"><div class="mini-brand__mark"></div><div class="mini-brand__name">Copper Vale LLC</div><div class="mini-brand__tagline">(AN EQUINE CONGLOMERATE)</div></div>
    <div class="address-band">
      <div class="address address--va">4120 Maple Hollow Way<br>Riverton, VA 22950</div>
      <div class="address-band__rule"></div>
      <div class="address address--fl">2750 SE 112<sup>th</sup> Terrace<br>Pinecrest, FL 32690</div>
    </div>
  </section>

</main>
</body>
</html>
```